International ecosystem needs business model upgrade

We need an upgrade from our business model. We already have a sketch that needs be 'upgraded'. Ugraded means better colors, smoother lines. It needs to be more attractive. We would like to see the use of colour blue and white aspects. It must remain simple.

If you want extra information about the model. Feel free to contact me. The words in the model are written in Dutch. See below descriptions for more specific information about this project.

Summit Circle is a cross sectoral network of more than 400 CEO’s/General Managers within The Netherlands. Members are all responsible for large or medium sized organizations. The goal of the network is to enable cross sectoral learning as well as establish collaborations and business deals between its members. In order to realize this the business matching team of the Summit Circle organization proactively initiates value adding introductions between its members. Furthermore Summit Circle organizes a wide range of masterclasses, round tables, dinners and company visits.

Target Market(s)

CEO, Directors

Industry/Entity Type

Business

Font styles to use
Sans Serif

Colors
85cae6
33a6d7
ffffff
0355a3
000000

Requirements
Must have
• The model has to be understandable (not to complex).
• The file attatched should be used as a basis.
Nice to have
• A model without text would be prefferable. We can add texts later.
Should not have
• Extra text

```html
<!DOCTYPE html>
<html lang="en">
<head>
<meta charset="utf-8">
<title>Summit Circle – Accelerator Model</title>
<link rel="stylesheet" href="https://fonts.googleapis.com/css2?family=Source+Sans+3:wght@400;600;700&display=swap">
<style>
  :root {
    --blue-deep: #0355a3;
    --blue-mid: #33a6d7;
    --blue-light: #85cae6;
    --blue-core: #a3d5ec;
    --white: #ffffff;
    --ink: #000000;
    --leader-line: #555555;
    --accent: #f9a93b;
  }
  html, body {
    margin: 0;
    padding: 0;
    width: 1200px;
    height: 841px;
    overflow: hidden;
    background: var(--white);
  }
  .model {
    display: block;
    width: 1200px;
    height: 841px;
    font-family: "Source Sans 3", sans-serif;
  }
  .ring-outer { fill: var(--blue-deep); }
  .segment-mid { fill: var(--blue-mid); }
  .segment-light { fill: var(--blue-light); }
  .core { fill: var(--blue-core); }
  .banner-input { fill: var(--blue-deep); }
  .banner-intake { fill: var(--blue-mid); }
  .arm-edge { fill: none; stroke: var(--accent); stroke-width: 3; stroke-linejoin: miter; }
  .flow-arrow { fill: var(--accent); }
  .leader { fill: none; stroke: var(--leader-line); stroke-width: 2; }
  .leader-dot { fill: var(--white); stroke: var(--leader-line); stroke-width: 2; }
  .label { fill: var(--ink); font-size: 14px; font-weight: 600; text-anchor: middle; }
  .label-head { fill: var(--ink); font-size: 13px; font-weight: 700; text-anchor: middle; letter-spacing: 0.3px; }
  .banner-title { fill: var(--white); font-size: 23px; font-weight: 700; letter-spacing: 0.5px; }
  .banner-text { fill: var(--white); font-size: 12.5px; font-weight: 700; }
  .core-title { fill: var(--white); font-size: 21px; font-weight: 700; text-anchor: middle; }
</style>
</head>
<body>
<svg class="model" viewBox="0 0 1165 816" role="img" aria-label="Summit Circle accelerator model">
  <defs>
    <path id="curve-input" d="M 456 130 Q 578 90 700 130"/>
    <path id="curve-intake-1" d="M 462 201 Q 578 164 694 201"/>
    <path id="curve-intake-2" d="M 470 216 Q 578 183 686 216"/>
    <path id="curve-intake-3" d="M 478 231 Q 578 201 678 231"/>
  </defs>

  <!-- Network ring -->
  <g class="network-ring">
    <path class="ring-outer" d="M 718.9 140.1 A 300 300 0 1 1 437.1 140.1 L 447.5 237.9 A 212 212 0 1 0 708.5 237.9 Z"/>
    <path class="segment-mid" d="M 842.1 306.2 A 282 282 0 0 1 846.9 489.8 L 797.4 474.2 A 230 230 0 0 0 793.4 324.5 Z"/>
    <path class="segment-light" d="M 842.1 503.8 A 282 282 0 0 1 694.9 661.6 L 673.4 614.3 A 230 230 0 0 0 793.4 485.5 Z"/>
    <path class="segment-mid" d="M 681.4 667.4 A 282 282 0 0 1 474.6 667.4 L 493.7 619.0 A 230 230 0 0 0 662.3 619.0 Z"/>
    <path class="segment-light" d="M 461.1 661.6 A 282 282 0 0 1 313.9 503.8 L 362.6 485.5 A 230 230 0 0 0 482.6 614.3 Z"/>
    <path class="segment-mid" d="M 309.1 489.8 A 282 282 0 0 1 313.9 306.2 L 362.6 324.5 A 230 230 0 0 0 358.6 474.2 Z"/>
    <path class="arm-edge" d="M 405.9 159.2 L 437.1 140.1 L 447.5 237.9"/>
    <path class="arm-edge" d="M 750.1 159.2 L 718.9 140.1 L 708.5 237.9"/>
  </g>

  <!-- Input and intake -->
  <g class="input-flow">
    <text class="label-head" x="578" y="68">INPUT</text>
    <path class="banner-input" d="M 445 102 Q 578 62 712 102 L 694 152 Q 578 116 462 152 Z"/>
    <text class="banner-title"><textPath href="#curve-input" startOffset="50%" text-anchor="middle">YOU AS A LEADER</textPath></text>
    <path class="flow-arrow" d="M 574 128 h 6 v 7 h 5 l -8 9 l -8 -9 h 5 Z"/>
    <text class="label-head" x="578" y="157">INTAKE</text>
    <path class="banner-intake" d="M 450 188 Q 578 150 706 188 L 682 238 Q 578 210 474 238 Z"/>
    <text class="banner-text"><textPath href="#curve-intake-1" startOffset="50%" text-anchor="middle">Inventarisation of organizational</textPath></text>
    <text class="banner-text"><textPath href="#curve-intake-2" startOffset="50%" text-anchor="middle">chaellenges, ambitions</textPath></text>
    <text class="banner-text"><textPath href="#curve-intake-3" startOffset="50%" text-anchor="middle">and personal development needs</textPath></text>
    <path class="flow-arrow" d="M 574 225 h 6 v 6 h 5 l -8 9 l -8 -9 h 5 Z"/>
  </g>

  <!-- Core team -->
  <g class="core-team">
    <circle class="core" cx="578" cy="398" r="152"/>
    <text class="core-title" x="578" y="382">Summit Circle</text>
    <text class="core-title" x="578" y="410">Accelerator Team</text>
  </g>

  <!-- Exchange arrows -->
  <g class="exchange-arrows">
    <path class="flow-arrow" d="M 364 397 l 12 -11 v 7 h 28 v -7 l 12 11 l -12 11 v -7 h -28 v 7 Z"/>
    <path class="flow-arrow" d="M 738 392 l 12 -11 v 7 h 28 v -7 l 12 11 l -12 11 v -7 h -28 v 7 Z"/>
    <path class="flow-arrow" d="M 576 551 l 11 12 h -7 v 28 h 7 l -11 12 l -11 -12 h 7 v -28 h -7 Z"/>
  </g>

  <!-- Callouts -->
  <g class="callouts">
    <path class="leader" d="M 183 125 H 345 L 405 184"/>
    <circle class="leader-dot" cx="410" cy="189" r="5"/>
    <text class="label-head" x="262" y="82">OUTPUT</text>
    <text class="label" x="262" y="100">Spot on break</text>
    <text class="label" x="262" y="117">through Insights</text>

    <path class="leader" d="M 975 125 H 805 L 749 184"/>
    <circle class="leader-dot" cx="744" cy="189" r="5"/>
    <text class="label-head" x="893" y="82">OUTPUT</text>
    <text class="label" x="893" y="100">Spot on value</text>
    <text class="label" x="893" y="117">adding contacts</text>

    <path class="leader" d="M 57 327 H 250 L 311 389"/>
    <circle class="leader-dot" cx="315" cy="393" r="5"/>
    <text class="label" x="163" y="270">Universities</text>
    <text class="label" x="163" y="288">(over 1000 best in class</text>
    <text class="label" x="163" y="305">professors and</text>
    <text class="label" x="163" y="322">thought leaders)</text>

    <path class="leader" d="M 1070 325 H 905 L 845 385"/>
    <circle class="leader-dot" cx="841" cy="389" r="5"/>
    <text class="label" x="985" y="299">Start up accelerators</text>
    <text class="label" x="985" y="316">(over 5000 start ups)</text>

    <path class="leader" d="M 115 512 H 310 L 384 568"/>
    <circle class="leader-dot" cx="388" cy="572" r="5"/>
    <text class="label" x="190" y="488">Media</text>
    <text class="label" x="190" y="505">(online and offline)</text>

    <path class="leader" d="M 1052 527 H 850 L 766 571"/>
    <circle class="leader-dot" cx="762" cy="575" r="5"/>
    <text class="label" x="967" y="503">Thought Leaders</text>
    <text class="label" x="967" y="520">(accros the world)</text>

    <path class="leader" d="M 808 718 H 645 L 582 657"/>
    <circle class="leader-dot" cx="578" cy="653" r="5"/>
    <text class="label" x="722" y="712">500 CEO’s</text>
  </g>
</svg>
</body>
</html>
```